Energy Company 8-page Brochure

We are in need of a redesign of our 8-page brochure. Attached is the initial design that does not represent us very well. We are looking for CLEAN/CORPORATE look with a little bit of flair (graphs/charts if applicable).

I prefer white background and our company colors (blue/green) to be the accent colors. Feel free to add additional accent colors to highlight certain areas.

We are in the energy field (not just solar), so please consider the types of images that you will use. Are headquarters is located in Chicago, IL so a great looking picture of the skyline or something similar would work for the front and back cover.

We have additional marketing collateral that we will want to be uniformed once we have the right design.

Good luck, and we look forward to receiving some great designs!

Best Regards,
Rob

Target Market(s)

Small to large businesses (B2B).

Industry/Entity Type

It Company

Colors
ffffff
9bcb3c
0255a3

Requirements
Must have
• Clean design, company colors, specified content and editable files.
Nice to have
• Graphs, charts, highlighted areas where necessary.
Should not have
• Clutter! Please utilized page space appropriately. There is a lot of content, so you need to consider graphics and image placement.

```html
<!DOCTYPE html>
<html lang="en">
<head>
<meta charset="utf-8">
<title>Brightline – LED Lighting Spread</title>
<link href="https://fonts.googleapis.com/css2?family=Questrial&display=swap" rel="stylesheet">
<style>
  :root {
    --white: #ffffff;
    --brand-green: #9bcb3c;
    --brand-blue: #0255a3;
    --accent-blue: #4a7fc1;
    --accent-red: #ee2a36;
    --accent-coral: #ef5a63;
    --chart-dark: #4a4a4a;
    --text-dark: #3d3d3d;
    --text-mid: #666666;
    --chip-grey: #ececec;
    --gutter: rgba(0,0,0,0.12);
  }
  * { box-sizing: border-box; margin: 0; padding: 0; }
  html, body { width: 1200px; height: 800px; overflow: hidden; background: var(--white); }
  body { font-family: "Questrial", sans-serif; color: var(--text-dark); }

  .spread { position: relative; width: 1200px; height: 800px; display: flex; }
  .page { position: relative; width: 600px; height: 800px; background: var(--white); overflow: hidden; }
  .page--left { box-shadow: inset -18px 0 24px -18px var(--gutter); }
  .page--right { box-shadow: inset 18px 0 24px -18px var(--gutter); }

  /* left page */
  .hero-photo {
    position: absolute; left: 0; top: 0; width: 600px; height: 380px;
    background: radial-gradient(circle at 72% 62%, #e8f4f8 0, #7fc0d8 9%, #1f7aa6 32%, #0d4f78 70%, #083a5c 100%);
  }
  .brand {
    position: absolute; left: 392px; top: 346px; display: flex; align-items: center; gap: 8px;
    background: var(--white); padding: 6px 10px;
  }
  .brand__mark { width: 22px; height: 22px; background: var(--brand-green); }
  .brand__name { font-size: 20px; color: var(--brand-blue); }
  .product-photo {
    position: absolute; left: 515px; top: 318px; width: 72px; height: 110px; border-radius: 36px 36px 14px 14px;
    background: linear-gradient(180deg, #f4f4f4 0%, #d5d8da 60%, #a9adb0 100%);
  }

  .accent-blocks { position: absolute; width: 44px; }
  .accent-blocks__blue { height: 56px; background: var(--accent-blue); }
  .accent-blocks__green { height: 30px; background: var(--brand-green); }
  .page--left .accent-blocks { left: 22px; top: 394px; }
  .page--right .accent-blocks { left: 24px; top: 532px; }

  .section-label { position: absolute; left: 78px; top: 398px; font-size: 17px; color: var(--brand-green); }
  .headline { position: absolute; font-size: 29px; line-height: 1.08; color: var(--text-dark); font-weight: 400; }
  .page--left .headline { left: 78px; top: 420px; width: 420px; }
  .page--right .headline { left: 84px; top: 532px; width: 400px; font-size: 27px; }

  .body-copy {
    position: absolute; font-size: 9.6px; line-height: 1.42; text-align: justify; color: var(--text-mid);
  }
  .page--left .body-copy { left: 36px; top: 520px; width: 530px; }
  .page--right .body-copy { left: 24px; top: 652px; width: 552px; }

  .pull-quote {
    position: absolute; left: 40px; top: 692px; width: 520px; text-align: center;
    font-size: 19px; line-height: 1.2; color: var(--text-dark);
  }

  /* right page */
  .cashflow-chart { position: absolute; left: 0; top: 0; width: 600px; height: 265px; }
  .chart-title { font-size: 14px; fill: var(--text-mid); }
  .chart-figure { font-size: 15px; fill: var(--text-mid); }
  .chart-note { font-size: 11px; fill: var(--text-mid); }
  .chart-stage { font-size: 8px; fill: var(--text-mid); letter-spacing: 0.5px; }
  .chart-inset { font-size: 15px; fill: var(--white); }

  .solar-photo {
    position: absolute; left: 0; top: 265px; width: 600px; height: 245px;
    background:
      radial-gradient(circle at 42% 18%, #fffbe6 0, #f6e3b0 6%, rgba(220,200,160,0.6) 16%, rgba(120,130,150,0) 40%),
      linear-gradient(160deg, #7f8ea8 0%, #3d5a85 45%, #23395c 80%, #182840 100%);
  }
</style>
</head>
<body>
<main class="spread">

  <section class="page page--left">
    <div class="hero-photo" role="img" aria-label="Row of hanging light bulbs against a blue wall, one LED bulb glowing"></div>
    <div class="brand"><span class="brand__mark"></span><span class="brand__name">Brightline</span></div>
    <div class="product-photo" role="img" aria-label="Product shot of an LED bulb with aluminium heat sink"></div>

    <div class="accent-blocks"><div class="accent-blocks__blue"></div><div class="accent-blocks__green"></div></div>
    <p class="section-label">LED</p>
    <h2 class="headline">The major factor<br>driving the transition to<br>LED is economic.</h2>

    <p class="body-copy">LED lighting solutions have become an increasingly attractive option for businesses because, in addition to lowering energy use, they also deliver strong financial and maintenance savings. By embracing LED lighting, your company leads by example in corporate responsibility, improves working conditions and raises productivity for employees. The quality and performance of LED lighting has improved steadily while costs keep falling. With a lifespan between 75,000 and 100,000 hours, LED is now the clear low-cost choice on a lifecycle basis. LEDs give higher quality light, contain no mercury and emit no UV radiation. Less time on the ladder means your maintenance team can focus on other needs. Not all LEDs are created equal. We only provide competitively priced quality products that make sense for our customers.</p>

    <p class="pull-quote">Consultancy Halden Advisory has estimated that the LED market will grow more than 700% to almost $84.9 billion by 2020</p>
  </section>

  <section class="page page--right">
    <svg class="cashflow-chart" viewBox="0 0 600 265" aria-label="Expenses and cash flow before, during and after a lighting retrofit">
      <defs>
        <marker id="arrowhead" markerWidth="8" markerHeight="8" refX="6" refY="4" orient="auto">
          <path d="M0,0 L8,4 L0,8 Z" fill="#222"/>
        </marker>
        <radialGradient id="chip" cx="40%" cy="35%" r="70%">
          <stop offset="0" stop-color="#ffffff"/><stop offset="1" stop-color="#d9d9d9"/>
        </radialGradient>
      </defs>

      <text class="chart-title" x="24" y="24">Expenses and cash flow for a lighting retrofit of</text>
      <text class="chart-title" x="24" y="42">a logistics facility</text>

      <!-- before -->
      <circle cx="88" cy="168" r="46" fill="var(--accent-coral)"/>
      <text class="chart-inset" x="88" y="166" text-anchor="middle">$625,000</text>
      <text class="chart-inset" x="88" y="184" text-anchor="middle">To Utility</text>
      <circle cx="96" cy="232" r="25" fill="url(#chip)" stroke="#cfcfcf"/>
      <text class="chart-stage" x="96" y="235" text-anchor="middle">BEFORE</text>

      <!-- during -->
      <g transform="translate(218,140) scale(1.2)">
        <path d="M0,0 L0,-40 A40,40 0 0 1 39.68,5.01 Z" fill="var(--accent-red)"/>
        <path d="M0,0 L39.68,5.01 A40,40 0 0 1 -29.16,27.39 Z" fill="var(--accent-blue)"/>
        <path d="M0,0 L-29.16,27.39 A40,40 0 0 1 0,-40 Z" fill="var(--chart-dark)"/>
      </g>
      <circle cx="224" cy="210" r="25" fill="url(#chip)" stroke="#cfcfcf"/>
      <text class="chart-stage" x="224" y="213" text-anchor="middle">DURING</text>
      <line x1="195" y1="125" x2="150" y2="105" stroke="#222" stroke-width="2" marker-end="url(#arrowhead)"/>
      <text class="chart-figure" x="104" y="76">$231,250</text>
      <text class="chart-figure" x="112" y="94">To Utility</text>
      <line x1="240" y1="125" x2="288" y2="102" stroke="#222" stroke-width="2" marker-end="url(#arrowhead)"/>
      <text class="chart-figure" x="302" y="108">$168,750</text>
      <text class="chart-figure" x="318" y="126">To Brightline</text>
      <line x1="250" y1="160" x2="282" y2="180" stroke="#222" stroke-width="2" marker-end="url(#arrowhead)"/>
      <text class="chart-figure" x="292" y="178">$225,000</text>
      <text class="chart-note" x="292" y="194">Cash flow to</text>
      <text class="chart-note" x="292" y="207">company</text>

      <!-- after -->
      <g transform="translate(440,92) scale(1.25)">
        <path d="M0,0 L0,-40 A40,40 0 1 1 -29.16,27.39 Z" fill="var(--accent-red)"/>
        <path d="M0,0 L-29.16,27.39 A40,40 0 0 1 0,-40 Z" fill="var(--chart-dark)"/>
      </g>
      <circle cx="404" cy="158" r="25" fill="url(#chip)" stroke="#cfcfcf"/>
      <text class="chart-stage" x="404" y="161" text-anchor="middle">AFTER</text>
      <line x1="440" y1="60" x2="490" y2="30" stroke="#222" stroke-width="2" marker-end="url(#arrowhead)"/>
      <text class="chart-figure" x="498" y="22">$231,250</text>
      <text class="chart-figure" x="504" y="40">To Utility</text>
      <line x1="470" y1="115" x2="505" y2="135" stroke="#222" stroke-width="2" marker-end="url(#arrowhead)"/>
      <text class="chart-figure" x="510" y="152">$393,750</text>
      <text class="chart-note" x="510" y="168">Cash flow to</text>
      <text class="chart-note" x="510" y="181">company</text>
    </svg>

    <div class="solar-photo" role="img" aria-label="Close view of solar panels with the sun flaring across them"></div>

    <div class="accent-blocks"><div class="accent-blocks__blue"></div><div class="accent-blocks__green"></div></div>
    <h2 class="headline">Lower your usage and lower your costs while increasing your bottom line.</h2>

    <p class="body-copy">Is it really possible to reduce energy consumption by a significant percentage with no out-of-pocket expense? The answer is yes. Our team has the expertise to understand complicated markets and the resources to secure the best prices. We review your supply, negotiate on your behalf and improve the efficiency of major building systems such as lighting, heating, ventilation and air conditioning. Owners who want to cut energy use and costs often lack the available capital. Brightline provides an innovative solution that funds the upgrade, so you benefit from lower bills, a smaller carbon footprint and immediate savings.</p>
  </section>

</main>
</body>
</html>
```